Path of Ember and Willow web design template. Spiritual services and courses and workshops

This is a new company and would like a modern design. I run courses and workshops, meditation classes and provide healing and reading services.
Updates

Project Deadline Extended
Reason: Only one designer has submitted and there are others who have accepted my invitation but not yet submitted designs.

Target Market(s)

Non gender specific. Ages 25-60

Industry/Entity Type

It Company

Requirements
Must have
• Looking to have a earthy feel as the bulk of my work is shamanic based. e.g. of a picture on top would be an Australian outback scene with rocks, red earth, ghost gum tree.

The tab titles are: Home, About Us, Workshops, Services, Courses, Contact Us.

Design to have the capabilities for adding different features e.g. booking online, Coinbrook payments, connection to Chatterly. I need to add/modify/delete details e.g. course dates, locations etc.Calendar. (if this is possible to have as well I will adjust the budget)

Nice to have
• Would like a simple design not too busy looking. Clean and fresh. I was after a picture/logo/company name on the top. Horizontal drop down menus. Ability to add links, pictures, articles. But I am open to different concepts.

```html
<!DOCTYPE html>
<html lang="en">
<head>
<meta charset="utf-8">
<title>Path of Ember and Willow</title>
<link rel="stylesheet" href="https://fonts.googleapis.com/css2?family=PT+Sans:wght@400;700&family=Arimo:wght@400;700&display=swap">
<style>
  :root {
    --cream: #fbf3d6;
    --cream-light: #fdf8e6;
    --orange: #f08a24;
    --rust: #b4461a;
    --brown-dark: #5a2a10;
    --brown-footer: #983a0b;
    --brown-footer-deep: #8a3207;
    --text-body: #3b2a1c;
    --nav-text: #4a2410;
    --white: #ffffff;
    --olive: #a8a032;
    --hero-light: #d9a066;
    --hero-mid: #b8672a;
    --hero-deep: #7a3f1a;
  }
  * { box-sizing: border-box; margin: 0; padding: 0; }
  html, body { width: 1172px; height: 1200px; overflow: hidden; background: var(--cream); }
  body { font-family: "Arimo", Arial, sans-serif; color: var(--text-body); }
  .page { position: relative; width: 1172px; height: 1200px; overflow: hidden; }

  /* Header */
  .site-header {
    position: absolute; left: 0; top: 0; width: 100%; height: 156px;
    background: linear-gradient(180deg, var(--cream) 0%, var(--cream-light) 100%);
    border-top: 4px solid var(--olive);
  }
  .brand {
    position: absolute; left: 56px; top: 106px;
    display: flex; align-items: center; gap: 8px;
    font-family: "PT Sans", sans-serif; font-weight: 700; font-size: 15px;
    color: var(--rust);
  }
  .brand-mark { width: 14px; height: 14px; background: var(--orange); }
  .book-online {
    position: absolute; left: 902px; top: 22px; width: 214px; height: 48px;
    display: flex; border-radius: 3px; overflow: hidden;
    box-shadow: 0 2px 3px rgba(0,0,0,0.25);
  }
  .book-online .arrow {
    width: 52px; background: var(--brown-dark);
    display: flex; align-items: center; justify-content: center;
  }
  .book-online .label {
    flex: 1; background: linear-gradient(180deg, #b84f12, #9c3a08);
    color: var(--white); font-family: "PT Sans", sans-serif; font-size: 20px;
    display: flex; align-items: center; padding-left: 12px;
  }
  .main-nav {
    position: absolute; right: 58px; top: 116px;
    display: flex; gap: 42px;
    font-family: "PT Sans", sans-serif; font-weight: 700; font-size: 15.5px;
  }
  .main-nav a { color: var(--nav-text); text-decoration: none; }
  .main-nav a.active { color: var(--orange); }

  /* Hero */
  .hero { position: absolute; left: 0; top: 156px; width: 100%; height: 559px; }
  .hero-photo {
    position: absolute; inset: 0;
    background: linear-gradient(160deg, var(--hero-light) 0%, var(--hero-mid) 55%, var(--hero-deep) 100%);
  }
  .hero-title {
    position: absolute; left: 104px; top: 372px;
    color: var(--white); font-family: "PT Sans", sans-serif; font-size: 66px; font-weight: 400;
    letter-spacing: 1px; line-height: 1;
  }
  .hero-text {
    position: absolute; left: 104px; top: 461px; width: 960px;
    color: var(--white); font-size: 15.5px; line-height: 19px;
  }
  .hero-dots { position: absolute; left: 506px; top: 526px; display: flex; gap: 5px; }
  .hero-dots span { width: 13px; height: 13px; border-radius: 50%; background: #f4ead8; }
  .hero-dots span.current { background: var(--white); border: 3px solid var(--rust); }
  .hero-rule {
    position: absolute; left: 0; top: 715px; width: 100%; height: 3px;
    background: linear-gradient(90deg, var(--orange), var(--olive));
  }

  /* Content */
  .content { position: absolute; left: 0; top: 718px; width: 100%; height: 304px; background: var(--cream); }
  .column { position: absolute; top: 34px; }
  .column h2 {
    font-family: "PT Sans", sans-serif; font-weight: 400; font-size: 22px; color: var(--rust);
    padding-bottom: 6px; display: inline-block;
    border-bottom: 2px dotted var(--orange);
  }
  .about { left: 42px; width: 333px; }
  .about p { margin-top: 12px; font-size: 14.5px; line-height: 21px; text-align: justify; }
  .courses { left: 468px; width: 236px; }
  .courses ul { list-style: none; margin-top: 6px; }
  .courses li {
    font-weight: 700; font-size: 15px; letter-spacing: 0.4px; padding: 8px 0 9px;
    border-bottom: 1px solid #e8dcbc;
  }
  .courses li:last-child { border-bottom: none; }
  .workshops { left: 809px; width: 293px; }
  .workshops h2 { margin-left: 5px; }
  .event {
    display: flex; height: 47px; margin-top: 11px; border: 1px solid #e4d6b4;
    border-radius: 3px; overflow: hidden; background: var(--cream-light);
  }
  .event:first-of-type { margin-top: 18px; }
  .event-date {
    width: 84px; background: var(--orange); color: var(--white); font-size: 17px;
    display: flex; align-items: center; justify-content: center;
  }
  .event-title { display: flex; align-items: center; padding-left: 12px; font-size: 14.5px; }
  .read-more {
    position: absolute; top: 231px; width: 112px; height: 36px;
    background: var(--brown-dark); color: var(--white); font-size: 16px;
    display: flex; align-items: center; justify-content: center; border-radius: 2px;
  }

  /* Footer */
  .site-footer {
    position: absolute; left: 0; top: 1022px; width: 100%; height: 178px;
    background: linear-gradient(180deg, var(--brown-footer), var(--brown-footer-deep));
    color: var(--white);
  }
  .footer-heading { position: absolute; font-family: "PT Sans", sans-serif; font-size: 23px; font-weight: 400; }
  .newsletter-title { left: 52px; top: 21px; }
  .field {
    position: absolute; height: 26px; background: var(--white); border-radius: 2px;
    color: #9a9a9a; font-size: 14.5px; padding-left: 10px; display: flex; align-items: center;
  }
  .join {
    position: absolute; left: 297px; top: 99px; width: 68px; height: 38px;
    background: #6a2c0c; color: var(--white); font-size: 19px; border-radius: 2px;
    display: flex; align-items: center; justify-content: center;
  }
  .footer-links { position: absolute; left: 41px; top: 148px; font-size: 14px; word-spacing: 2px; }
  .social-title { left: 588px; top: 23px; }
  .social { position: absolute; left: 586px; display: flex; align-items: center; gap: 14px;
    font-family: "PT Sans", sans-serif; font-weight: 700; font-size: 24px; }
  .social-square { width: 32px; height: 32px; border: 2px solid var(--white); border-radius: 3px; }
  .footer-brand {
    position: absolute; left: 892px; top: 86px; width: 240px; text-align: center;
    font-family: "PT Sans", sans-serif; font-weight: 700; font-size: 15px; color: var(--orange);
  }
  .copyright {
    position: absolute; left: 892px; top: 138px; width: 240px; text-align: center;
    font-size: 12px; line-height: 16px;
  }
</style>
</head>
<body>
<div class="page">
  <header class="site-header">
    <div class="brand"><span class="brand-mark"></span>Path of Ember and Willow</div>
    <div class="book-online">
      <div class="arrow">
        <svg width="20" height="20" viewBox="0 0 20 20"><path d="M5 2 L15 10 L5 18 L5 13 L9 10 L5 7 Z" fill="#ffffff"/></svg>
      </div>
      <div class="label">BOOK ONLINE</div>
    </div>
    <nav class="main-nav">
      <a class="active" href="#">HOME</a>
      <a href="#">ABOUT US</a>
      <a href="#">WORKSHOPS</a>
      <a href="#">SERVICES</a>
      <a href="#">COURSES</a>
      <a href="#">CONTACT US</a>
    </nav>
  </header>

  <section class="hero">
    <div class="hero-photo" role="img" aria-label="Landscape photograph of sandstone cliffs above the sea at sunset"></div>
    <h1 class="hero-title">LOREM IPSUM DOLOR SIT AMET</h1>
    <p class="hero-text">Lorem ipsum dolor sit amet, quo agam debet semper ex, has no doctus facilisi indoctum. Magna errem vulputate eu his, vel cu illud dolore. Primis accumsan no sea. Ponderum disputando duo ea, vix omnium placerat consectetuer at. Cu vim putent persius.</p>
    <div class="hero-dots"><span class="current"></span><span></span><span></span><span></span></div>
  </section>
  <div class="hero-rule"></div>

  <main class="content">
    <section class="column about">
      <h2>ABOUT US</h2>
      <p>Lorem ipsum dolor sit amet, quo agam debet semper ex, has no doctus facilisi indoctum. Magna errem vulputate eu his, vel cu illud dolore. Primis accumsan no sea. Ponderum disputando duo ea, vix omnium placerat consectetuer at. Cu vim putent persius.</p>
    </section>
    <a class="read-more" style="left:41px">Read more</a>

    <section class="column courses">
      <h2>COURSES OFFERED</h2>
      <ul>
        <li>&gt; Lorem ipsum dolor sit amet</li>
        <li>&gt; Lorem ipsum dolor sit amet</li>
        <li>&gt; Lorem ipsum dolor sit amet</li>
        <li>&gt; Lorem ipsum dolor sit amet</li>
      </ul>
    </section>
    <a class="read-more" style="left:467px">Read more</a>

    <section class="column workshops">
      <h2>WORKSHOPS</h2>
      <div class="event"><div class="event-date">1 Feb</div><div class="event-title">Lorem ipsum dolor sit amet</div></div>
      <div class="event"><div class="event-date">1 Feb</div><div class="event-title">Lorem ipsum dolor sit amet</div></div>
    </section>
    <a class="read-more" style="left:810px">Read more</a>
  </main>

  <footer class="site-footer">
    <h3 class="footer-heading newsletter-title">Subscribe for Newsletter</h3>
    <div class="field" style="left:50px;top:65px;width:148px">Name</div>
    <div class="field" style="left:210px;top:65px;width:149px">Last name</div>
    <div class="field" style="left:52px;top:105px;width:245px">Email</div>
    <div class="join">Join</div>
    <div class="footer-links">Home &nbsp;| &nbsp;About Us &nbsp;| &nbsp;Workshops &nbsp;| &nbsp;Services &nbsp;| &nbsp;Courses &nbsp;| &nbsp;Contact Us</div>

    <h3 class="footer-heading social-title">Socialise</h3>
    <div class="social" style="top:66px"><span class="social-square"></span>Chatterly</div>
    <div class="social" style="top:111px"><span class="social-square"></span>Chirpline</div>

    <div class="footer-brand">Path of Ember and Willow</div>
    <p class="copyright">Copyright 2013 Path of Ember and Willow.<br>All rights reserved.</p>
  </footer>
</div>
</body>
</html>
```